Online Advice via Video Site requires Cutting Edge Homepage

We need a creative new and exciting webdesign for our tutoring via video-chat website.

We have prepared a "demo" homepage for you to see various promotional material that we think would be suitable for the homepage. http://www.learnvista.example/demo

The actual site is undergoing some final tinkering but can be accessed and used at http://www.learnvista.example

There is NO NEED to take any colours or design structure from this.

We expect the logo to be changed to match the new site. The new logo should match the site's function.

I have included some other projects that we like the look of:
http://www.artmarketplace.example/design/143762
http://www.artmarketplace.example/design/561630
http://www.artmarketplace.example/design/247199
http://www.artmarketplace.example/design/255195
http://www.boldfinch.example/

Target Market(s)

People that will work as tutors/advisers or be student/clients

Industry/Entity Type

Tutoring

Requirements
Must have
• The search is the main feature of the homepage

After the search the next goal of the page is to get people to sign up to the site

Login, (optional inclusion of the chatterly login - if you don't include it then you need only have a "login" button... no username or password input fields)

Footer
Nice to have
• The promotional material for the site, the colours on the Slydo file CAN BE changed to suit the new design you propose.

```html
<!DOCTYPE html>
<html lang="en">
<head>
<meta charset="utf-8">
<title>LearnVista — Home</title>
<link href="https://fonts.googleapis.com/css2?family=PT+Sans+Narrow:wght@400;700&family=Open+Sans:wght@400;600&family=Tinos:wght@400;700&display=swap" rel="stylesheet">
<style>
:root{
  --page:#51667a;
  --shell:#e7e8ea;
  --panel:#f4f5f7;
  --bar-top:#4d8fc8;
  --bar-bottom:#1d5584;
  --tab:#2b6190;
  --ink-blue:#2b5f8a;
  --link-blue:#2e6aa6;
  --ink-dark:#1f3446;
  --muted:#5d7183;
  --grey-bar:#8595a7;
  --accent:#e8321c;
  --white:#ffffff;
}
*{box-sizing:border-box;margin:0;padding:0}
html,body{width:1200px;height:1090px;overflow:hidden}
body{background:var(--page);position:relative;font-family:"PT Sans Narrow",sans-serif;color:var(--ink-dark)}
.abs{position:absolute}
.account{top:20px;left:955px;display:flex;gap:26px;color:var(--white);font-size:16px;font-weight:700}
.account span{display:flex;align-items:center;gap:6px}
.shell{left:50px;top:108px;width:1097px;height:933px;background:var(--shell);border-radius:12px}
.masthead{left:62px;top:61px;width:1072px;height:77px;border-radius:8px;background:linear-gradient(var(--bar-top),var(--bar-bottom));border:1px solid #2a5d88}
.brand{left:84px;top:76px;display:flex;align-items:center;gap:14px;color:var(--white);font-family:"Tinos",serif;font-weight:700;font-size:38px}
.brand i{width:40px;height:40px;border-radius:50%;background:var(--white);display:block}
.nav{left:529px;top:79px;display:flex;gap:8px;align-items:center}
.nav a{background:var(--tab);color:#e9f1f8;text-decoration:none;font-family:"Tinos",serif;font-size:16px;height:32px;display:flex;align-items:center;justify-content:center;border-radius:3px 3px 0 0}
.search-panel{left:72px;top:150px;width:1051px;height:233px;background:var(--panel);border-radius:10px}
.search-label{left:234px;top:208px;font-size:32px;font-weight:700;color:var(--ink-blue)}
.search-input{left:343px;top:201px;width:435px;height:50px;border:2px solid #cfd4da;border-radius:8px;background:var(--white)}
.search-btn{left:801px;top:199px;width:223px;height:52px;border-radius:8px;background:linear-gradient(#5a93c4,#245c8c);border:2px solid #8eb0cc;color:var(--white);font-size:21px;font-weight:700;display:flex;align-items:center;justify-content:center}
.tagline{left:192px;top:272px;width:873px;height:34px;border-left:4px solid #cfd3d8;border-right:4px solid #cfd3d8;font-family:"Open Sans",sans-serif;font-size:17px;display:flex;align-items:center;justify-content:center;color:var(--ink-dark)}
.points{font-size:15px;font-weight:700;color:var(--link-blue);list-style:none}
.points li{display:flex;align-items:center;gap:12px;height:27px}
.points li::before,.diamond::before{content:"";width:11px;height:11px;background:#2a4d6c;transform:rotate(45deg);display:block}
.video{left:75px;top:397px;width:574px;height:270px;background:#030303}
.video-title{left:0;top:90px;width:574px;text-align:center;font-size:38px;color:#1d1d1d}
.controls{left:0;bottom:0;width:574px;height:48px;background:#1b2836}
.clients{left:658px;top:400px;width:467px;height:267px;background:#ebecee;border:1px solid #d6d9dd;border-radius:8px}
.tab-label{left:683px;top:389px;width:95px;height:37px;background:var(--panel);border:1px solid #cfd3d8;border-radius:8px;font-size:18px;font-weight:700;letter-spacing:1px;display:flex;align-items:center;justify-content:center}
.client-list{list-style:none;font-weight:700;letter-spacing:.5px}
.client-list li{display:flex;align-items:center;gap:10px;height:26px}
.client-list li::before{content:"";width:9px;height:9px;border:1.5px solid #8b97a3;transform:rotate(45deg)}
.client-list .main{color:var(--link-blue);font-size:16px}
.client-list .sub{color:#44515c;font-size:14px;padding-left:61px}
.client-list .sub::before{background:#a6aeb6}
.read-more{left:1015px;top:620px;width:95px;height:38px;background:var(--white);border:1px solid #cfd3d8;border-radius:8px;font-size:15px;font-weight:700;display:flex;align-items:center;justify-content:center}
.features{left:80px;top:693px;width:664px;height:269px;background:var(--panel);border-radius:8px}
.feature-tab{top:680px;width:146px;height:85px;background:var(--panel);border:1px solid #d6d9dd;border-radius:6px;font-size:19px;font-weight:700;letter-spacing:1px;color:var(--ink-blue);text-align:center;line-height:22px;display:flex;align-items:center;justify-content:center}
.feature-tab.active{color:var(--accent)}
.feature-body{left:99px;top:772px;width:631px;height:176px;background:var(--white);border-radius:4px}
.feature-lines{left:173px;top:820px;font-size:16px;font-weight:700;letter-spacing:1px;line-height:26px;color:var(--ink-dark)}
.topics{left:755px;top:693px;width:365px;height:269px;background:var(--panel);border-radius:6px}
.topics-head{left:760px;top:697px;width:360px;height:35px;background:var(--grey-bar);color:var(--white);font-size:16px;font-weight:700;letter-spacing:1.5px;display:flex;align-items:center;padding-left:21px}
.topics-photo{left:935px;top:733px;width:185px;height:228px;background:linear-gradient(90deg,#f4f5f7 0%,#b9c3cf 35%,#5f6e80 100%)}
.topic-list{list-style:none;font-size:17px;font-weight:700;letter-spacing:1px;color:#141e26}
.topic-list li{display:flex;align-items:center;gap:12px;height:32px}
.topic-list li::before{content:"";width:9px;height:9px;border:1.5px solid #6f7b86;transform:rotate(45deg)}
.footer{left:62px;top:988px;width:1072px;height:76px;border-radius:8px;background:linear-gradient(var(--bar-top),var(--bar-bottom));border:1px solid #2a5d88}
.footer-links{left:108px;top:1000px;font-family:"Tinos",serif;font-size:16px;color:#e3edf6}
.credit{left:262px;top:1025px;font-family:"Tinos",serif;font-size:15px;color:#e3edf6}
.social{left:924px;top:1010px;display:flex;gap:14px}
.social i{width:32px;height:32px;border-radius:50%;background:var(--white);border:3px solid #cfe0ee;display:block}
</style>
</head>
<body>
<div class="abs account">
  <span><svg width="26" height="30" viewBox="0 0 26 30"><circle cx="8" cy="8" r="6" fill="none" stroke="#e6c14a" stroke-width="3"/><path d="M12 12l10 14M17 19l4-2M19 23l3-2" stroke="#c9cdd2" stroke-width="3"/></svg>Login</span>
  <span><svg width="28" height="30" viewBox="0 0 28 30"><circle cx="12" cy="8" r="6" fill="#e9b07a"/><path d="M2 28c0-9 5-12 10-12s10 3 10 12z" fill="#2f6fb2"/><circle cx="22" cy="22" r="5" fill="#3aa63a"/><path d="M22 19v6M19 22h6" stroke="#fff" stroke-width="2"/></svg>Register</span>
</div>

<div class="abs shell"></div>

<header class="abs masthead"></header>
<div class="abs brand"><i></i>LearnVista</div>
<nav class="abs nav">
  <svg width="32" height="30" viewBox="0 0 32 30" style="margin-right:8px"><path d="M16 3L3 15h4v12h7v-8h4v8h7V15h4z" fill="#e8f1fa" stroke="#2f6fae" stroke-width="2"/></svg>
  <a style="width:101px">Student</a>
  <a style="width:101px">Advisors</a>
  <a style="width:109px">Topics</a>
  <a style="width:101px">About us</a>
  <a style="width:102px">Technology</a>
</nav>

<section class="abs search-panel"></section>
<div class="abs search-label">SEARCH</div>
<div class="abs search-input"></div>
<div class="abs search-btn">Search Topics &amp; Advisors</div>
<p class="abs tagline">Imagine if, whenever you have a problem, you could discuss it instantly with the&nbsp; experts on that topic</p>
<ul class="abs points" style="left:212px;top:318px">
  <li>LearnVista is the place for e-learning, mentoring &amp; professional advice</li>
  <li>It instantly connects people with knowledge and those who need it</li>
</ul>
<ul class="abs points" style="left:681px;top:316px">
  <li>Connects people for ongoing advice or on off answers</li>
  <li>Ask questions and/or work exactly when it suits you</li>
</ul>

<div class="abs video" role="img" aria-label="Promotional video player">
  <div class="abs video-title">Do you know something ?</div>
  <svg class="abs" style="left:254px;top:88px" width="56" height="50" viewBox="0 0 56 50"><ellipse cx="28" cy="25" rx="26" ry="23" fill="none" stroke="#8a8a8a" stroke-width="2.5"/><path d="M20 12l20 13-20 13z" fill="#8a8a8a"/></svg>
  <div class="abs controls">
    <svg width="574" height="48" viewBox="0 0 574 48">
      <rect x="8" y="7" width="56" height="34" fill="#0f1822"/><path d="M30 16l12 8-12 8z" fill="#fff"/>
      <rect x="75" y="12" width="345" height="24" fill="#0f1822"/><rect x="84" y="22" width="276" height="4" fill="#d9d9d9"/><rect x="84" y="22" width="50" height="4" fill="#d0231c"/>
      <text x="368" y="28" font-size="9" fill="#ddd" font-family="Open Sans">00:08 / 00:46</text>
      <rect x="442" y="12" width="78" height="24" fill="#0f1822"/><path d="M449 20h4l4-4v16l-4-4h-4z" fill="#fff"/><rect x="463" y="21" width="2" height="6" fill="#d0231c"/><path d="M468 21v6M472 21v6M476 21v6M480 21v6M484 21v6M488 21v6M492 21v6M496 21v6M500 21v6M504 21v6" stroke="#ddd" stroke-width="2"/>
      <rect x="530" y="12" width="34" height="24" fill="#0f1822"/><rect x="539" y="18" width="16" height="12" fill="none" stroke="#ddd" stroke-width="1.5"/>
    </svg>
  </div>
</div>

<section class="abs clients"></section>
<div class="abs tab-label">CLIENTS</div>
<ul class="abs client-list" style="left:711px;top:457px">
  <li class="main">Get online guidance instantly</li>
  <li class="main">&nbsp;Got a tough issue or need some direction?</li>
  <li class="sub">Shortlist mentors, ask if they can help</li>
  <li class="sub">Get instant results</li>
  <li class="sub">Pay only for the tutor's time you use</li>
  <li class="main">&nbsp;Need ongoing advice?</li>
</ul>
<div class="abs read-more">Read More</div>

<section class="abs features"></section>
<div class="abs feature-tab" style="left:99px">Instant<br>Personal Advice</div>
<div class="abs feature-tab" style="left:257px">IDirect Video<br>Conference</div>
<div class="abs feature-tab" style="left:415px">Advisors or<br>Clients</div>
<div class="abs feature-tab active" style="left:575px">PayWallet or<br>Credit Card</div>
<div class="abs feature-body"></div>
<svg class="abs" style="left:631px;top:757px" width="44" height="24" viewBox="0 0 44 24"><path d="M0 0h44L22 24z" fill="#1f5f94"/></svg>
<div class="abs feature-lines">
  Charges based on individual advisor's rate<br>
  Pay only for the time you use<br>
  Pay via paywallet or credit card<br>
  Be paid via credit card
</div>
<svg class="abs" style="left:564px;top:814px" width="100" height="96" viewBox="0 0 100 96"><circle cx="50" cy="48" r="46" fill="#e6c82b" stroke="#c9a815" stroke-width="3"/></svg>
<div class="abs" style="left:532px;top:913px;display:flex;gap:8px">
  <i style="width:43px;height:26px;background:#1a3c8c;display:block"></i>
  <i style="width:40px;height:26px;background:#e2452a;display:block"></i>
  <i style="width:28px;height:26px;background:#2f86c8;display:block"></i>
  <i style="width:40px;height:26px;background:#3c3c3c;display:block"></i>
</div>

<section class="abs topics"></section>
<div class="abs topics-photo" role="img" aria-label="Photo of a business team meeting around a laptop"></div>
<div class="abs topics-head">ADVISORS BY TOPICS</div>
<ul class="abs topic-list" style="left:786px;top:753px">
  <li>English</li>
  <li>Building</li>
  <li>Cultural Studies</li>
  <li>Criminology</li>
  <li>Agriculture</li>
  <li>Veterinary Science</li>
</ul>

<footer class="abs footer"></footer>
<div class="abs footer-links">Home | Student | Advisors | Topics | Blog | FAQs | Sitemap | About us | Our Technology | Contact</div>
<div class="abs credit">Web Designed &amp; Development By Northgate Webworks</div>
<div class="abs social"><i></i><i></i><i></i><i style="width:26px;height:26px;margin-top:3px"></i></div>
</body>
</html>
```